60 Ways to de-stress Poster

I would like a poster ( A4 full colour) with a list of 60 ways to destress. I would like the design to be clean and stylish (not cartoonish)

My Target market is stressed out mums so I want the poster to feel inspirational and relaxing to look at.

I have added a sample of something I like - but open to other ideas

Finished art would be print ready pdf

Target Market(s)

Mums who are stressed out - mainly new mums. I want this to be a poster that someone would happily put up that looks more like artwork.

Requirements
Must have
• My logo elements and colours but happy to incorporate other colours that blend well into it.

Colours:
Bright green: Pantone 376
Bright green as CMYK: c: 45.2% m: 0% y: 100% k: 0%

Logo text large grey: 70% black
Logo text strapline: 75% black
Tree: 80% black

Fonts:
Logo 'Willowbank Haven': Verdana
Logo 'Counselling & coaching services for mums': Gill Sans Light
Should not have
• No cartoonish images - I want it very clean and stylish

```html
<!DOCTYPE html>
<html lang="en">
<head>
<meta charset="utf-8">
<title>60 Ways to De Stress – Willowbank Haven</title>
<link rel="stylesheet" href="https://fonts.googleapis.com/css2?family=Open+Sans:wght@400;600;800&family=Delius&display=swap">
<style>
  :root {
    --teal: #4ec1b5;
    --green: #8cc63f;
    --grey: #555657;
    --grey-soft: #6b6c6d;
    --paper: #ececec;
    --page: #ffffff;
    --cloud-font: "Delius", "Comic Neue", sans-serif;
    --head-font: "Open Sans", Verdana, sans-serif;
  }
  * { margin: 0; padding: 0; box-sizing: border-box; }
  html, body { width: 1200px; height: 1000px; overflow: hidden; background: var(--page); }
  .canvas { position: relative; width: 1200px; height: 1000px; }
  .poster {
    position: absolute; left: 285px; top: 45px; width: 637px; height: 900px;
    background: var(--paper);
  }
  .title { position: absolute; left: 285px; width: 637px; text-align: center; font-family: var(--head-font); line-height: 1; }
  .title-number { top: 78px; font-size: 132px; font-weight: 800; color: var(--teal); letter-spacing: -4px; }
  .title-lead { top: 197px; font-size: 30px; font-weight: 800; color: var(--green); }
  .title-main { top: 226px; font-size: 29px; font-weight: 400; color: var(--grey); letter-spacing: 0.5px; }

  .tips { list-style: none; }
  .tip { position: absolute; font-family: var(--cloud-font); line-height: 1; white-space: nowrap; letter-spacing: -0.2px; }
  .tip.tight { letter-spacing: -0.5px; }
  .tip.teal { color: var(--teal); }
  .tip.green { color: var(--green); }
  .tip.grey { color: var(--grey); }
  .tip.up { writing-mode: vertical-rl; transform: rotate(180deg); }

  .brand { position: absolute; left: 490px; top: 864px; font-family: var(--head-font); }
  .brand-name { font-size: 20px; font-weight: 600; color: var(--grey); line-height: 1; }
  .brand-line { margin-top: 5px; font-size: 11.5px; font-weight: 400; color: var(--grey-soft); }
  .brand-dot { position: absolute; left: 678px; top: 866px; width: 16px; height: 16px; border-radius: 50%; background: var(--green); }
</style>
</head>
<body>
<main class="canvas">
  <div class="poster"></div>

  <h1>
    <span class="title title-number">60</span>
    <span class="title title-lead">WAYS TO</span>
    <span class="title title-main">DE STRESS</span>
  </h1>

  <ul class="tips">
    <li class="tip teal" style="left:490px;top:287px;font-size:22px">put on some music and dance</li>
    <li class="tip green" style="left:500px;top:316px;font-size:18px">light a scented candle</li>
    <li class="tip green" style="left:710px;top:315px;font-size:12px">write a poem</li>
    <li class="tip grey tight" style="left:493px;top:339px;font-size:15.5px">take a mini mental holiday</li>
    <li class="tip teal" style="left:712px;top:332px;font-size:14px">fake a smile</li>
    <li class="tip grey up" style="left:682px;top:312px;font-size:18px">make a gratitude list</li>
    <li class="tip grey" style="left:712px;top:351px;font-size:13px">gaze at the</li>
    <li class="tip grey" style="left:712px;top:364px;font-size:29px">stars</li>
    <li class="tip teal tight" style="left:486px;top:360px;font-size:15.5px">swing on a&nbsp; swing</li>
    <li class="tip green" style="left:614px;top:365px;font-size:11px">hug someone</li>
    <li class="tip teal" style="left:460px;top:382px;font-size:12px">go to the park</li>
    <li class="tip green" style="left:546px;top:382px;font-size:12px">take a nap</li>
    <li class="tip grey" style="left:625px;top:384px;font-size:14px">write in</li>
    <li class="tip grey" style="left:625px;top:401px;font-size:13px">a journal</li>
    <li class="tip teal up" style="left:605px;top:385px;font-size:11px">call or visit a friend</li>
    <li class="tip teal" style="left:708px;top:397px;font-size:17px">pat a dog</li>
    <li class="tip grey" style="left:447px;top:401px;font-size:19px">listening to music</li>
    <li class="tip green tight" style="left:477px;top:425px;font-size:13.5px">buy yourself flowers</li>
    <li class="tip green" style="left:624px;top:422px;font-size:14px">meditate</li>
    <li class="tip green" style="left:706px;top:419px;font-size:17px">volunteer</li>
    <li class="tip teal" style="left:706px;top:437px;font-size:17px">your time</li>
    <li class="tip grey tight" style="left:468px;top:444px;font-size:13px">take some deep breaths</li>
    <li class="tip teal" style="left:624px;top:440px;font-size:25px">have</li>
    <li class="tip teal" style="left:624px;top:466px;font-size:18px">a bath</li>
    <li class="tip teal" style="left:704px;top:459px;font-size:12px">make yourself</li>
    <li class="tip teal" style="left:704px;top:476px;font-size:14px">a cup of tea</li>
    <li class="tip green" style="left:446px;top:460px;font-size:26px">go for a walk</li>
    <li class="tip teal up tight" style="left:422px;top:458px;font-size:15px">watch the clouds go by</li>
    <li class="tip grey up" style="left:444px;top:496px;font-size:11px">stand up and stretch</li>
    <li class="tip grey tight" style="left:462px;top:492px;font-size:14px">plant a tree</li>
    <li class="tip teal tight" style="left:540px;top:491px;font-size:15px">eat something mindfully</li>
    <li class="tip green" style="left:700px;top:497px;font-size:12px">play in the park</li>
    <li class="tip teal" style="left:462px;top:512px;font-size:16px">paint a picture</li>
    <li class="tip grey" style="left:573px;top:512px;font-size:16px">forgive someone</li>
    <li class="tip grey" style="left:701px;top:515px;font-size:12px">get a massage</li>
    <li class="tip grey tight" style="left:462px;top:535px;font-size:16px">review your achievements</li>
    <li class="tip teal up tight" style="left:655px;top:532px;font-size:11.5px">go for a bike ride</li>
    <li class="tip teal" style="left:677px;top:531px;font-size:17px">get a haircut</li>
    <li class="tip grey" style="left:585px;top:555px;font-size:20px">create</li>
    <li class="tip grey" style="left:585px;top:573px;font-size:20px">some</li>
    <li class="tip grey" style="left:585px;top:591px;font-size:18px">routines</li>
    <li class="tip teal tight" style="left:463px;top:559px;font-size:16px">take a long drive</li>
    <li class="tip grey tight" style="left:677px;top:553px;font-size:11.5px">colour in a picture</li>
    <li class="tip green" style="left:677px;top:568px;font-size:17px">take a class</li>
    <li class="tip green" style="left:677px;top:588px;font-size:17px">at the gym</li>
    <li class="tip grey" style="left:463px;top:580px;font-size:20px">read a book</li>
    <li class="tip grey up tight" style="left:772px;top:550px;font-size:12.5px">watch a funny movie</li>
    <li class="tip teal" style="left:423px;top:607px;font-size:17px">play a game</li>
    <li class="tip green tight" style="left:529px;top:610px;font-size:15px">bake some cookies</li>
    <li class="tip grey" style="left:677px;top:612px;font-size:13px">go on a picnic</li>
    <li class="tip grey tight" style="left:425px;top:632px;font-size:13px">perform&nbsp; an act of kindness</li>
    <li class="tip green tight" style="left:588px;top:633px;font-size:12px">give yourself a time-out</li>
    <li class="tip green" style="left:727px;top:629px;font-size:17px">vent</li>
    <li class="tip green up" style="left:420px;top:657px;font-size:15px">de-clutter a drawer</li>
    <li class="tip teal tight" style="left:440px;top:653px;font-size:14px">listen to a guided relaxation mp3</li>
    <li class="tip grey" style="left:655px;top:650px;font-size:20px">ask for help</li>
    <li class="tip grey" style="left:439px;top:673px;font-size:20px">disconnect from technology</li>
    <li class="tip green" style="left:692px;top:679px;font-size:12px">live for today</li>
    <li class="tip green" style="left:438px;top:701px;font-size:12px">look at a work of art</li>
    <li class="tip green" style="left:567px;top:697px;font-size:20px">visit a farmers market</li>
    <li class="tip teal" style="left:438px;top:720px;font-size:14px">borrow&nbsp; a book from the library</li>
    <li class="tip green tight" style="left:641px;top:722px;font-size:11px">accept what you can't change</li>
    <li class="tip grey" style="left:438px;top:740px;font-size:13px">scale down your to do list</li>
    <li class="tip teal tight" style="left:609px;top:740px;font-size:12px">write positive self-statements</li>
    <li class="tip grey" style="left:438px;top:758px;font-size:15px">outsource if you can</li>
    <li class="tip green tight" style="left:587px;top:759px;font-size:13px">try progressive muscle relaxation</li>
    <li class="tip teal" style="left:443px;top:780px;font-size:29px">compliment yourself often</li>
  </ul>

  <footer>
    <div class="brand">
      <p class="brand-name">Willowbank Haven</p>
      <p class="brand-line">counselling &amp; coaching for mums</p>
    </div>
    <span class="brand-dot"></span>
  </footer>
</main>
</body>
</html>
```